TAVRO Capital Group LLC a High Risk Big Rewards company for Rich Young Entrepreneurs

We would like a very modern, powerful in the eyes of our customers, modern, minimalist feel, financial gain. this business card is for young Rich entrepreneurs who want to invest money into High Risk, Big Rewards Businesses. The card Should sell the business!! let your creativity go Wild! I pick most of the designers for this project because of your BOLD Designs, I would like this card to be Bold, Modern, Minimalist, use as many effects in your graphic Artist Mind, Do not let the Financial sound of this business to make you think Conservative that's the last thing we are! if you have a lot of money and you want to play a risky market call US
Updates

Project Deadline Extended
Reason: have not received, enough designs to choose 1st and second place, sure I have received over 100 designs but it seems most designers are submitting every card they have ever made before and calling it mine, please we are looking for fresh ideas please!

Target Market(s)

Private Risky Investors

Industry/Entity Type

Financial

Contact Information for Business Card

powerful in the eyes of our customers,modern, minimalist feel

Font styles to use
Other font styles liked:
• Modern feeling fonts

Requirements
Must have
• The Company Name is TAVRO Capital Group LLC and it must be on the CARD
• My Name, title, Cell , email
• Delvin Ashcroft G.E.D.
• Managing Member
• 555.038.6195
• delvin@tavrocapitalgroup.example
Nice to have
• try a black thick plastic card with round corners with Delvin Ashcroft GED (make sure GED is smaller than name) just on one side of the card, and my phone number with out the icons and email on the other side, this card should look like a exclusive credit card or exclusive VIP card, something you would never loose

```html
<!DOCTYPE html>
<html lang="en">
<head>
<meta charset="utf-8">
<title>TAVRO Capital Group LLC — Business Card</title>
<link rel="stylesheet" href="https://fonts.googleapis.com/css2?family=Nunito+Sans:wght@700;800;900&display=swap">
<style>
  :root {
    --backdrop: #e3e8ea;
    --card-navy: #25215a;
    --accent-glow: #4a4790;
    --ink-white: #ffffff;
  }
  * { margin: 0; padding: 0; box-sizing: border-box; }
  html, body {
    width: 1200px;
    height: 900px;
    overflow: hidden;
    background: var(--backdrop);
  }
  .stage {
    position: relative;
    width: 1200px;
    height: 900px;
  }
  .business-card {
    position: absolute;
    left: 180px;
    top: 205px;
    width: 840px;
    height: 490px;
    background: var(--card-navy);
    overflow: hidden;
    font-family: "Nunito Sans", "Avenir Next", Arial, sans-serif;
    color: var(--ink-white);
  }
  .edge-accent {
    position: absolute;
    top: 0;
    bottom: 0;
    width: 110px;
  }
  .edge-accent--left {
    left: 0;
    background: linear-gradient(to right, var(--accent-glow), var(--card-navy));
  }
  .edge-accent--right {
    right: 0;
    background: linear-gradient(to left, var(--accent-glow), var(--card-navy));
  }
  .card-details {
    position: absolute;
    left: 113px;
    top: 0;
    right: 60px;
  }
  .company-name {
    position: absolute;
    top: 94px;
    font-size: 21px;
    font-weight: 800;
    letter-spacing: 0.02em;
    text-transform: uppercase;
    white-space: nowrap;
  }
  .holder-name {
    position: absolute;
    top: 148px;
    font-size: 41px;
    font-weight: 800;
    letter-spacing: 0.035em;
    text-transform: uppercase;
    white-space: nowrap;
    line-height: 1.1;
  }
  .holder-credential {
    font-size: 0.6em;
    letter-spacing: 0.04em;
    margin-left: 0.15em;
  }
  .holder-title {
    position: absolute;
    top: 207px;
    font-size: 18px;
    font-weight: 800;
    letter-spacing: 0.01em;
    text-transform: uppercase;
    white-space: nowrap;
  }
  .phone {
    position: absolute;
    top: 274px;
    font-size: 41px;
    font-weight: 800;
    letter-spacing: 0.01em;
    white-space: nowrap;
  }
  .email {
    position: absolute;
    top: 350px;
    font-size: 29px;
    font-weight: 800;
    white-space: nowrap;
  }
</style>
</head>
<body>
  <main class="stage">
    <section class="business-card" aria-label="TAVRO Capital Group LLC business card">
      <div class="edge-accent edge-accent--left" role="img" aria-label="White burst ray decoration along the left edge"></div>
      <div class="edge-accent edge-accent--right" role="img" aria-label="White burst ray decoration along the right edge"></div>

      <div class="card-details">
        <p class="company-name">TAVRO Capital Group LLC</p>
        <h1 class="holder-name">Delvin Ashcroft <span class="holder-credential">G.E.D</span></h1>
        <p class="holder-title">Managing Member</p>
        <p class="phone">555.038.6195</p>
        <p class="email">delvin@tavrocapitalgroup.example</p>
      </div>
    </section>
  </main>
</body>
</html>
```